Visitenkarten und Briefpapier für Beratungsunternehmen
Zielgruppe
Führungskräfte im Gesundheits- und Sozialwesen-
Aufgabenstellung
Wir suchen ein Set aus Briefpapier und Visitenkarten zu umserem Logo. Beides darf (muss nicht) beidseitig gestaltet werden.

```html
<!DOCTYPE html>
<html lang="de">
<head>
<meta charset="utf-8">
<title>Kelmaran – Briefpapier und Visitenkarte</title>
<link rel="stylesheet" href="https://fonts.googleapis.com/css2?family=Arimo:wght@400;700&family=Italianno&display=swap">
<style>
  :root{
    --bg:#ece6dc;
    --paper:#ffffff;
    --green-dark:#2e7d1c;
    --green:#4aa51f;
    --green-pale:#c9e9a6;
    --blue:#1f3f8f;
    --ink:#111111;
    --sig:#2233cc;
    --white:#ffffff;
  }
  *{box-sizing:border-box;margin:0;padding:0}
  html,body{width:1200px;height:1200px;overflow:hidden;background:var(--bg);font-family:"Arimo",Arial,sans-serif;color:var(--ink)}
  .canvas{position:relative;width:1200px;height:1200px}

  .wordmark{position:absolute;display:flex;align-items:center;gap:10px;color:var(--white);font-weight:700;letter-spacing:.5px}
  .wordmark-dot{width:14px;height:14px;border-radius:50%;background:var(--white)}

  /* Letterhead */
  .letter{position:absolute;left:110px;top:75px;width:742px;height:1003px;background:var(--paper);box-shadow:0 2px 10px rgba(0,0,0,.18);overflow:hidden}
  .letter-head{position:absolute;left:0;top:0;width:742px;height:170px}
  .letter .wordmark{left:98px;top:62px;font-size:34px}
  .head-contact{position:absolute;right:82px;top:24px;text-align:right;color:var(--white);font-size:10.5px;font-weight:700;line-height:13px}
  .head-contact .company{font-size:15px;line-height:17px}
  .head-contact .legal{font-size:7.5px;font-weight:400;line-height:9px;margin-bottom:12px}
  .sender-line{position:absolute;left:98px;top:180px;font-size:7.5px;text-decoration:underline}
  .recipient{position:absolute;left:98px;top:199px;font-size:13.5px;line-height:16.5px;font-style:normal}
  .date{position:absolute;right:82px;top:199px;font-size:13.5px}
  .letter-body{position:absolute;left:98px;top:342px;width:562px;font-size:13px;line-height:16.5px;text-align:justify}
  .letter-body h1{font-size:15.5px;font-weight:700;margin-bottom:37px;text-align:left}
  .letter-body p{margin-bottom:16.5px}
  .letter-body .closing{margin-bottom:2px}
  .signature{font-family:"Italianno",cursive;color:var(--sig);font-size:30px;line-height:28px}
  .letter-foot{position:absolute;left:0;bottom:0;width:742px;height:100px}
  .foot-cols{position:absolute;left:98px;right:82px;bottom:14px;display:flex;justify-content:space-between;color:var(--white);font-size:9.5px;font-weight:700;line-height:12.5px}
  .foot-cols .mid{text-align:center}
  .foot-cols .right{text-align:right}

  /* Business cards */
  .card{position:absolute;left:800px;width:328px;height:190px;background:var(--paper);box-shadow:0 2px 8px rgba(0,0,0,.18);overflow:hidden}
  .card-front{top:286px}
  .card-back{top:500px}
  .card-front svg{position:absolute;left:0;top:0}
  .card-front .wordmark{left:84px;top:76px;font-size:30px}
  .card-person{position:absolute;left:22px;top:20px}
  .card-person .name{font-size:19px;font-weight:700;color:var(--blue);line-height:21px}
  .card-person .role{font-size:11.5px;font-weight:700;color:var(--green);line-height:14px}
  .card-contact{position:absolute;right:22px;top:28px;text-align:right;font-size:10.5px;line-height:13.5px}
  .card-back svg{position:absolute;left:0;bottom:0}
</style>
</head>
<body>
<div class="canvas">

  <section class="letter">
    <svg class="letter-head" viewBox="0 0 742 170" aria-hidden="true">
      <path d="M0 0H742V140Q371 175 0 150Z" fill="var(--green-dark)"/>
      <path d="M0 160Q371 185 742 150" fill="none" stroke="var(--green-pale)" stroke-width="4"/>
    </svg>
    <div class="wordmark"><span class="wordmark-dot"></span><span>KELMARAN</span></div>
    <div class="head-contact">
      <div class="company">Kelmaran UG</div>
      <div class="legal">(haftungsbeschränkt)</div>
      <div>Lindenweg 14 • 54321 Beispielstadt</div>
      <div>Fon: 0 98 76 / 54 32 10</div>
      <div>Fax: 0 98 76 / 54 32 11</div>
      <div>E-Mail: info@kelmaran.de</div>
      <div>www.kelmaran.de</div>
    </div>

    <div class="sender-line">Kelmaran UG (haftungsbeschränkt) • Lindenweg 14 • 54321 Beispielstadt</div>
    <address class="recipient">Herrn<br>Max Mustermann<br>Musterstraße 1<br>12345 Musterstadt</address>
    <div class="date">17.05.2010</div>

    <div class="letter-body">
      <h1>Gestaltung Ihrer Geschäftsbriefe und Visitenkarten</h1>
      <p>Sehr geehrte Damen und Herren,</p>
      <p>dies ist ein Typoblindtext. An ihm kann man sehen, ob alle Buchstaben da sind und wie sie aussehen. Manchmal benutzt man Worte wie Hamburgefonts, Rafgenduks oder Handgloves, um Schriften zu testen. Manchmal Sätze, die alle Buchstaben des Alphabets enthalten - man nennt diese Sätze »Pangrams«. Sehr bekannt ist dieser: The quick brown fox jumps over the lazy old dog.</p>
      <p>Oft werden in Typoblindtexte auch fremdsprachige Satzteile eingebaut (AVAIL® and Wefox™ are testing aussi la Kerning), um die Wirkung in anderen Sprachen zu testen. In Lateinisch sieht zum Beispiel fast jede Schrift gut aus. Quod erat demonstrandum. Seit 1975 fehlen in den meisten Testtexten die Zahlen, weswegen nach §204 TypoGb. ab dem Jahr 2034 Zahlen in 86 der Texte zur Pflicht werden. Nichteinhaltung wird mit bis zu 245 € oder 368 $ bestraft. Genauso wichtig in sind mittlerweile auch Âçcèñtë, die in neueren Schriften aber fast immer enthalten sind.</p>
      <p>Ein wichtiges aber schwierig zu integrierendes Feld sind OpenType-Funktionalitäten. Je nach Software und Voreinstellungen können eingebaute Kapitälchen, Kerning oder Ligaturen (sehr pfiffig) nicht richtig dargestellt werden.</p>
      <p class="closing">Mit freundlichem Gruß</p>
      <div class="signature">Renate Holler</div>
    </div>

    <svg class="letter-foot" viewBox="0 0 742 100" aria-hidden="true">
      <path d="M0 24Q371 0 742 24" fill="none" stroke="var(--green-pale)" stroke-width="4"/>
      <path d="M0 34Q371 12 742 34V100H0Z" fill="var(--green)"/>
    </svg>
    <div class="foot-cols">
      <div>Kelmaran UG (haftungsbeschränkt)<br>Lindenweg 14 • 54321 Beispielstadt<br>Geschäftsführerin: Renate Holler</div>
      <div class="mid">Hausbank Beispielstadt<br>Bankleitzahl 100 200 30<br>Kontonummer 123 456 789</div>
      <div class="right">Handelsregister: HRB 12345<br>Steuernummer: 200 / 4000 / 5000<br>Finanzamt Beispielstadt</div>
    </div>
  </section>

  <section class="card card-front">
    <svg width="328" height="190" viewBox="0 0 328 190" aria-hidden="true">
      <path d="M0 40Q164 20 328 30V140Q164 130 0 150Z" fill="var(--green-dark)"/>
      <path d="M0 160Q164 140 328 150" fill="none" stroke="var(--green-pale)" stroke-width="4"/>
    </svg>
    <div class="wordmark"><span class="wordmark-dot"></span><span>KELMARAN</span></div>
  </section>

  <section class="card card-back">
    <div class="card-person">
      <div class="name">Renate Holler</div>
      <div class="role">Geschäftsführerin</div>
    </div>
    <div class="card-contact">Lindenweg 14<br>54321 Beispielstadt<br>Fon: 0 98 76 / 54 32 10<br>Fax: 0 98 76 / 54 32 11<br>E-Mail: info@kelmaran.de<br>www.kelmaran.de</div>
    <svg width="328" height="60" viewBox="0 0 328 60" aria-hidden="true">
      <path d="M0 12Q164 0 328 12" fill="none" stroke="var(--green-pale)" stroke-width="4"/>
      <path d="M0 22Q164 10 328 22V60H0Z" fill="var(--green)"/>
    </svg>
  </section>

</div>
</body>
</html>
```